IT services company needs a business card designed

-2 sided business card.-Front is going to be the logo raised (3D floating effect) on a black background. Make the logos spider web shiny silver and keep the spider the same design. -Back needs to have the following information:Darrel Sotho, Managing Partner, Cell: 738-402-1954, Website: Plankhorn.com, Email: Darrel@Plankhorn.com
Target Market(s)
IT Services
Industry/Entity Type
It Company
Contact Information for Business Card
-2 sided business card.
-Front is going to be the logo raised (3D floating effect) on a black background. Make the logos spider web shiny silver and keep the spider the same design.
-Back needs to have the following information:
Darrel Sotho, Managing Partner, Cell: 738-402-1954, Website: Plankhorn.com, Email: Darrel@Plankhorn.com

```html
<!DOCTYPE html>
<html lang="en">
<head>
<meta charset="utf-8">
<title>Plankhorn business card</title>
<link rel="stylesheet" href="https://fonts.googleapis.com/css2?family=Abel&family=Bebas+Neue&display=swap">
<style>
  :root {
    --backdrop: #2b2b2d;
    --card: #1c2030;
    --accent: #4fc6f5;
    --wordmark: #c9cacd;
    --text: #d4d6da;
    --title: #c4c7cc;
  }
  * { margin: 0; padding: 0; box-sizing: border-box; }
  html, body { width: 1200px; height: 1200px; overflow: hidden; }
  body { background: var(--backdrop); position: relative; font-family: "Abel", sans-serif; }

  .card {
    position: absolute;
    left: 194px;
    width: 878px;
    height: 501px;
    background: var(--card);
    border-radius: 32px;
  }
  .card--contact { top: 35px; }
  .card--brand { top: 664px; }

  .wordmark {
    position: absolute;
    color: var(--wordmark);
    font-family: "Abel", sans-serif;
    letter-spacing: 2px;
    line-height: 1;
    white-space: nowrap;
    transform: translateX(-50%);
  }
  .card--contact .wordmark { left: 240px; top: 220px; font-size: 50px; }
  .card--brand .wordmark { left: 439px; top: 215px; font-size: 66px; }

  .divider {
    position: absolute;
    left: 437px;
    top: 159px;
    width: 3px;
    height: 180px;
    background: var(--accent);
  }

  .person { position: absolute; left: 510px; top: 150px; }
  .person__name {
    font-family: "Bebas Neue", sans-serif;
    font-size: 52px;
    line-height: 1;
    color: var(--accent);
    letter-spacing: 0.5px;
  }
  .person__title {
    margin-top: 4px;
    font-size: 21px;
    color: var(--title);
  }

  .contact-list { position: absolute; left: 510px; top: 262px; list-style: none; }
  .contact-list li {
    display: flex;
    align-items: center;
    height: 27px;
    font-size: 21px;
    color: var(--text);
  }
  .contact-list svg { width: 18px; height: 18px; margin-right: 31px; flex: none; }
</style>
</head>
<body>
  <section class="card card--contact">
    <div class="wordmark">PLANKHORN</div>
    <div class="divider"></div>
    <div class="person">
      <h1 class="person__name">DARREL SOTHO</h1>
      <p class="person__title">Managing Partner</p>
    </div>
    <ul class="contact-list">
      <li>
        <svg viewBox="0 0 24 24" aria-hidden="true"><path fill="var(--accent)" d="M6.6 10.8a15.1 15.1 0 0 0 6.6 6.6l2.2-2.2c.3-.3.7-.4 1-.2 1.1.4 2.3.6 3.6.6.6 0 1 .4 1 1V20c0 .6-.4 1-1 1A17 17 0 0 1 3 4c0-.6.4-1 1-1h3.5c.6 0 1 .4 1 1 0 1.3.2 2.5.6 3.6.1.3 0 .7-.2 1z"/></svg>
        738-402-1954
      </li>
      <li>
        <svg viewBox="0 0 24 24" aria-hidden="true"><rect x="2" y="5" width="20" height="14" fill="var(--accent)"/><path d="M2.5 5.5 12 13l9.5-7.5M2.5 18.5l7-6.5M21.5 18.5l-7-6.5" stroke="var(--card)" stroke-width="1.5" fill="none"/></svg>
        Darrel@Plankhorn.com
      </li>
      <li>
        <svg viewBox="0 0 24 24" aria-hidden="true" fill="none" stroke="var(--accent)" stroke-width="1.6"><circle cx="12" cy="12" r="9"/><ellipse cx="12" cy="12" rx="4" ry="9"/><path d="M3 12h18M4.5 7.5h15M4.5 16.5h15"/></svg>
        www.plankhorn.com
      </li>
    </ul>
  </section>

  <section class="card card--brand">
    <div class="wordmark">PLANKHORN</div>
  </section>
</body>
</html>
```